Kampagne Stuzzichini
Zielgruppe
Wir Haben ein Restaurant unsere Spezialität ist vorwiegend Italienischer Küche.
Für diese Kampagne wohlen wir hauptsächlich Firmenkunden und Leute duzu bewegen das Sie nach der arbeit, zu uns kommen um einen Apero Zu nehmen ansprechen.
Text:
STUZZICHINI (Überschrift)
Den typischen Apéro aus Italien gibt's Dienstags - Donnerstag ab 17.30 bis 19.00 Uhr zu jedem Getränk Gratis Dazu.
Von Foccacia über Oliven bis zu Lachsbrötchen- lassen Sie sich jede Woche von neuen Leckerbissen aus der Küche der Restaurant Tovelo überraschen!
Formate:
Postkarte A6
Volage ist vorhanden
Vorlage mit Verschnitt ist vorhanden.
-Booksmarke 75x210
Vorlage mit verschnitt ist vorhanden.
Ich lade verschiedenen Flyer hoch zur Orientation von style

```html
<!DOCTYPE html>
<html lang="de">
<head>
<meta charset="utf-8">
<title>Stuzzichini – Restaurant Tovelo</title>
<link rel="stylesheet" href="https://fonts.googleapis.com/css2?family=Encode+Sans+Condensed:wght@400&family=Parisienne&display=swap">
<style>
  :root {
    --wood-light: #dcc3a2;
    --wood-mid: #ccab86;
    --wood-dark: #b99470;
    --peach: #f2c48e;
    --brown: #4a3a30;
    --cream: #ffffff;
    --bg-dark: #7a5a4c;
    --coral: #f2765c;
    --coral-deep: #e25a44;
    --food-dark: #7a5444;
    --food-warm: #c8826a;
    --food-light: #e6cbb0;
    --food-mid: #b8947a;
  }
  html, body {
    margin: 0;
    padding: 0;
    overflow: hidden;
    background: #ffffff;
  }
  .postcard {
    position: relative;
    width: 1200px;
    height: 866px;
    overflow: hidden;
  }
  .postcard__art {
    position: absolute;
    inset: 0;
    display: block;
  }
  .headline {
    position: absolute;
    left: 60px;
    top: 112px;
    margin: 0;
    font-family: "Encode Sans Condensed", "Arial Narrow", sans-serif;
    font-weight: 400;
    font-size: 58px;
    letter-spacing: 1px;
    line-height: 1;
    color: var(--brown);
  }
  .offer {
    position: absolute;
    margin: 0;
    font-family: "Parisienne", cursive;
    font-weight: 400;
    color: var(--cream);
    line-height: 1;
    white-space: nowrap;
    text-shadow: 0 2px 6px rgba(0,0,0,0.25);
  }
  .offer--drink {
    left: 50px;
    top: 388px;
    font-size: 84px;
  }
  .offer--free {
    left: 292px;
    top: 548px;
    font-size: 70px;
  }
  .brand {
    position: absolute;
    left: 880px;
    top: 430px;
    width: 300px;
    text-align: center;
  }
  .brand__dot {
    display: block;
    width: 24px;
    height: 24px;
    margin: 0 auto 14px;
    border-radius: 50%;
    background: var(--brown);
  }
  .brand__name {
    font-family: "Encode Sans Condensed", "Arial Narrow", sans-serif;
    font-weight: 400;
    font-size: 32px;
    color: var(--brown);
    line-height: 1;
    white-space: nowrap;
  }
</style>
</head>
<body>
<main class="postcard">
  <svg class="postcard__art" viewBox="0 0 1200 866" width="1200" height="866">
    <defs>
      <linearGradient id="wood" x1="0" y1="0" x2="1" y2="0.3">
        <stop offset="0" stop-color="var(--wood-mid)"/>
        <stop offset="0.5" stop-color="var(--wood-light)"/>
        <stop offset="1" stop-color="var(--wood-dark)"/>
      </linearGradient>
      <linearGradient id="cocktails" x1="0" y1="0.6" x2="1" y2="0.2">
        <stop offset="0" stop-color="var(--bg-dark)"/>
        <stop offset="0.3" stop-color="#b0685a"/>
        <stop offset="0.55" stop-color="var(--coral)"/>
        <stop offset="1" stop-color="var(--coral-deep)"/>
      </linearGradient>
      <linearGradient id="food" x1="0" y1="0" x2="1" y2="1">
        <stop offset="0" stop-color="var(--food-dark)"/>
        <stop offset="0.3" stop-color="var(--food-warm)"/>
        <stop offset="0.65" stop-color="var(--food-light)"/>
        <stop offset="1" stop-color="var(--food-mid)"/>
      </linearGradient>
    </defs>

    <rect class="photo photo--food" x="0" y="480" width="1200" height="386" fill="url(#food)"
          role="img" aria-label="Foto: Apéro-Platte mit Lachsbrötchen, Crevetten, Oliven, Salami und Tomaten"/>

    <rect class="photo photo--cocktails" x="0" y="0" width="1200" height="515" fill="url(#cocktails)"
          role="img" aria-label="Foto: rote Cocktails im Martiniglas mit Zuckerrand und Limettenscheiben"/>

    <path class="band band--peach" d="M0,0 H730 C610,130 400,252 0,266 Z" fill="var(--peach)"/>
    <path class="panel panel--wood" d="M0,0 H710 C590,118 390,238 0,252 Z" fill="url(#wood)"/>

    <path class="band band--brown"
          d="M0,505 C220,490 470,484 660,490 C860,410 1050,260 1200,100 V842 C1060,662 880,562 690,520 C470,506 220,512 0,534 Z"
          fill="var(--brown)"/>
    <path class="panel panel--wood"
          d="M700,502 C880,425 1060,292 1200,140 V806 C1050,642 880,547 700,502 Z"
          fill="url(#wood)"/>
  </svg>

  <h1 class="headline">STUZZICHINI</h1>
  <p class="offer offer--drink">Getränk +</p>
  <p class="offer offer--free">Apero gratis dazu</p>

  <div class="brand">
    <span class="brand__dot"></span>
    <span class="brand__name">Restaurant Tovelo</span>
  </div>
</main>
</body>
</html>
```